Brightvale Fluid Systems Corp Business Cards

Business cards to match the logo.

Company is a start up water technology company that has developed a patented system using centrifugal force to separate waste from municipal waste water to produce crystal clear clean water. Product sell starting at 2 million to governments both in the US and international.

Business cards should have a professional look with the target generally engineers.

Target Market(s)

Engineers, Government officials and investors

Industry/Entity Type

Water Treatment

Contact Information for Business Card

Business cards design will be used for 6 to 8 people with job titles. Can use the quote "If there is magic in the planet, it is contained in water." but not required to use quote. Should follow theme of Logo

Font styles to use
Other font styles liked:
• match logo font

Requirements
Nice to have
• Colors to match Logo. Business cards to match style of flow of Logo.
• Emphasis on clean look not a busy look. Clean flowing water.
Should not have
• Pictures of industrial equipment or wastewater

```html
<!DOCTYPE html>
<html lang="en">
<head>
<meta charset="utf-8">
<title>Brightvale Fluid Systems – Business Cards</title>
<link href="https://fonts.googleapis.com/css2?family=Roboto:wght@400;500;700&display=swap" rel="stylesheet">
<style>
  :root{
    --bg:#e9edf1;
    --navy:#1c4a74;
    --blue-deep:#1f527f;
    --blue-mid:#2c78aa;
    --sky:#2d9bd8;
    --sky-soft:#8fc8ea;
    --paper:#fbfcfd;
    --ink:#4a4f55;
    --rule:#d4d9de;
  }
  *{box-sizing:border-box;margin:0;padding:0}
  html,body{width:1200px;height:786px;overflow:hidden}
  body{background:var(--bg);font-family:"Roboto",Arial,sans-serif;position:relative}

  .card{
    position:absolute;top:238px;width:540px;height:309px;border-radius:18px;overflow:hidden;
    box-shadow:0 10px 28px rgba(20,45,70,.18);
  }

  /* Front */
  .card--front{
    left:40px;
    background:linear-gradient(160deg,var(--blue-mid) 0%,var(--blue-deep) 60%,#1a4670 100%);
    color:#fff;display:flex;flex-direction:column;align-items:center;justify-content:center;text-align:center;
  }
  .front__name{font-weight:500;font-size:28px;letter-spacing:3px;line-height:1.15;text-transform:uppercase;color:#fff}
  .front__quote{margin-top:22px;font-size:13px;line-height:1.5;color:#e4eef6}

  /* Back */
  .card--back{left:620px;background:var(--paper)}
  .back__waves{position:absolute;left:0;top:0;width:540px;height:309px}
  .back__brand{
    position:absolute;left:60px;top:48px;width:200px;text-align:center;
    font-weight:500;font-size:20px;letter-spacing:2px;line-height:1.2;text-transform:uppercase;color:var(--navy);
  }
  .back__address{position:absolute;left:60px;top:122px;width:200px;text-align:center;font-size:12px;line-height:1.55;color:var(--ink)}
  .back__divider{position:absolute;left:288px;top:46px;width:1px;height:170px;background:var(--rule)}
  .person{position:absolute;left:312px;top:70px;width:210px}
  .person__name{font-weight:700;font-size:15px;letter-spacing:.5px;text-transform:uppercase;color:var(--sky)}
  .person__title{margin-top:4px;font-size:12px;line-height:1.4;color:var(--ink)}
  .contact{list-style:none;margin-top:16px}
  .contact__item{display:flex;align-items:center;gap:8px;font-size:12px;line-height:1.9;color:var(--ink)}
  .contact__icon{width:11px;height:11px;flex:none}
</style>
</head>
<body>

<section class="card card--front" aria-label="Card front">
  <p class="front__name">Brightvale<br>Fluid Systems</p>
  <p class="front__quote">If there is magic in the planet,<br>it is contained in water.</p>
</section>

<section class="card card--back" aria-label="Card back">
  <svg class="back__waves" viewBox="0 0 540 309" aria-hidden="true">
    <path d="M0 150 C60 200 170 250 300 309 L0 309 Z" fill="var(--sky)"/>
    <path d="M0 172 C70 222 180 262 285 309 L0 309 Z" fill="#e6ecf1"/>
    <path d="M0 184 C75 232 185 270 272 309 L0 309 Z" fill="var(--blue-deep)"/>
    <path d="M0 250 C90 270 180 290 232 309 L0 309 Z" fill="#184068"/>
  </svg>

  <p class="back__brand">Brightvale<br>Fluid Systems</p>
  <p class="back__address">2210 Harbor Crest Ave., Suite 204<br>Lakemont, FL 33910</p>
  <div class="back__divider"></div>

  <div class="person">
    <p class="person__name">Daniel Marlow</p>
    <p class="person__title">Member of Board of<br>Directors</p>
    <ul class="contact">
      <li class="contact__item">
        <svg class="contact__icon" viewBox="0 0 12 12"><path d="M3 1 L5 3.5 L4 5 C4.6 6.4 5.6 7.4 7 8 L8.5 7 L11 9 L9.5 11 C5 10.5 1.5 7 1 2.5 Z" fill="var(--sky)"/></svg>
        555-014-2870
      </li>
      <li class="contact__item">
        <svg class="contact__icon" viewBox="0 0 12 12"><rect x="1" y="2.5" width="10" height="7" rx="1" fill="var(--sky)"/><path d="M1.5 3 L6 6.5 L10.5 3" stroke="#fff" stroke-width="1" fill="none"/></svg>
        info@brightvalefs.com
      </li>
      <li class="contact__item">
        <svg class="contact__icon" viewBox="0 0 12 12"><circle cx="6" cy="6" r="5" fill="none" stroke="var(--sky)" stroke-width="1.2"/><ellipse cx="6" cy="6" rx="2.2" ry="5" fill="none" stroke="var(--sky)" stroke-width="1"/><path d="M1 6 H11" stroke="var(--sky)" stroke-width="1"/></svg>
        www.brightvalefs.com
      </li>
    </ul>
  </div>
</section>

</body>
</html>
```